Saffron Lantern Court Business Card

I am looking for a business card desgined for my restaurant. It is an Indian restaurant, we are looking for something thats modern, yet traditional with the indian culture, we are looking for colors that match our logo. The logo is a design of the building with the name of the restaurant. for more information on the restaurant go to www.saffronlanterncourt.example

Industry/Entity Type

Indian Restaurant

Contact Information for Business Card

we are looking for somthing thats modern, yet traditional with the indian culture, we are looking for colors that match our logo. The logo is a design of the building with the name of the restaurant. for more information on the restaurant go to www.saffronlanterncourt.example

Requirements
Must have
• The logo that is attached,
• Name: Harvinder Oberoi,
• address of the restaurant: 7328 West Larkspur Rd, Phoenix, Arizona, 85213
• Phone: (602) 555-0147
• Fax: (602) 555-0193
• Restaurant Catering Banquet
• Website: www.SaffronLanternCourt.example
Nice to have
• wanted to get something that goes with the theme of the restaurant, which is traditional but also keep a very professional and modern touch

```html
<!DOCTYPE html>
<html lang="en">
<head>
<meta charset="utf-8">
<title>Saffron Lantern Court – Business Card</title>
<link rel="stylesheet" href="https://fonts.googleapis.com/css2?family=Oswald:wght@500;600&family=Open+Sans:wght@700&display=swap">
<style>
  :root {
    --backdrop: #ece6de;
    --card: #ffffff;
    --red: #a3232a;
    --orange: #f15a24;
    --yellow: #fde428;
    --teal: #35b8b3;
    --brown: #2b1010;
  }
  * { margin: 0; padding: 0; box-sizing: border-box; }
  html, body { width: 1100px; height: 1200px; overflow: hidden; }
  body {
    position: relative;
    background: var(--backdrop);
    font-family: "Open Sans", Arial, sans-serif;
  }
  .card {
    position: absolute;
    width: 760px;
    height: 435px;
    background: var(--card);
    overflow: hidden;
  }
  .card-front { left: 176px; top: 133px; }
  .card-back  { left: 167px; top: 631px; }

  .front-pattern {
    position: absolute; inset: 0;
    background: radial-gradient(circle at 50% 50%,
      var(--orange) 0 6%, var(--yellow) 6% 30%, var(--orange) 30% 36%,
      var(--teal) 36% 52%, var(--brown) 52% 56%, var(--orange) 56% 100%);
  }

  .corner-ornament {
    position: absolute; left: 0; top: 0;
    width: 122px; height: 122px;
    border-radius: 0 0 100% 0;
    background: radial-gradient(circle at 15% 15%,
      var(--yellow) 0 35%, var(--orange) 35% 48%, var(--teal) 48% 100%);
  }

  .brand {
    position: absolute; left: 58px; top: 150px; width: 280px;
    text-align: center;
  }
  .brand-name {
    font-family: "Oswald", Arial, sans-serif;
    font-weight: 600;
    font-size: 52px;
    line-height: 62px;
    color: var(--red);
    text-transform: uppercase;
  }
  .brand-since {
    margin-top: 12px;
    font-size: 12px;
    letter-spacing: 3px;
    color: var(--red);
  }

  .person {
    position: absolute; right: 37px; top: 96px;
    text-align: right;
  }
  .person-name {
    font-family: "Oswald", Arial, sans-serif;
    font-weight: 500;
    font-size: 42px;
    line-height: 52px;
    color: var(--red);
    text-transform: uppercase;
    letter-spacing: 0.5px;
  }
  .person-rule {
    display: block; margin-top: 0; margin-left: auto;
    width: 253px; height: 8px;
  }

  .contact {
    position: absolute; right: 33px; top: 198px;
    list-style: none;
  }
  .contact-item {
    display: flex; justify-content: flex-end; align-items: center;
    height: 28px;
    font-size: 13.5px;
    color: var(--red);
  }
  .contact-icon {
    width: 22px; height: 22px; margin-left: 6px;
    border-radius: 4px; background: var(--orange);
    display: flex; align-items: center; justify-content: center;
  }
  .services {
    position: absolute; right: 35px; top: 286px;
    font-size: 15px;
    color: var(--red);
    text-transform: uppercase;
  }
</style>
</head>
<body>

  <section class="card card-front">
    <div class="front-pattern" role="img" aria-label="Full-bleed mandala flower pattern in orange, yellow, teal and dark brown"></div>
  </section>

  <section class="card card-back">
    <div class="corner-ornament" role="img" aria-label="Corner mandala flower ornament"></div>

    <div class="brand">
      <p class="brand-name">Saffron<br>Lantern<br>Court</p>
      <p class="brand-since">SINCE 1985</p>
    </div>

    <div class="person">
      <h1 class="person-name">Harvinder Oberoi</h1>
      <svg class="person-rule" viewBox="0 0 253 8" aria-hidden="true">
        <pattern id="dot-row" width="11.5" height="8" patternUnits="userSpaceOnUse">
          <circle cx="4" cy="4" r="3" fill="#f15a24"/>
        </pattern>
        <rect width="253" height="8" fill="url(#dot-row)"/>
      </svg>
    </div>

    <ul class="contact">
      <li class="contact-item">7328 West Larkspur Rd, Phoenix, Arizona, 85213
        <span class="contact-icon"><svg width="12" height="14" viewBox="0 0 12 14"><path d="M6 0a5 5 0 0 0-5 5c0 4 5 9 5 9s5-5 5-9a5 5 0 0 0-5-5z" fill="#fff"/><circle cx="6" cy="5" r="2" fill="#f15a24"/></svg></span>
      </li>
      <li class="contact-item">TEL: (602) 555-0147/FAX: (602) 555-0193
        <span class="contact-icon"><svg width="12" height="12" viewBox="0 0 12 12"><path d="M1 3c0-1.5 2-2 5-2s5 .5 5 2v1H8V3H4v1H1z" fill="#fff"/><rect x="2" y="5" width="8" height="6" rx="1" fill="#fff"/><circle cx="6" cy="8" r="1.5" fill="#f15a24"/></svg></span>
      </li>
      <li class="contact-item">www.SaffronLanternCourt.example
        <span class="contact-icon"><svg width="13" height="13" viewBox="0 0 14 14" fill="none" stroke="#fff" stroke-width="1.2"><circle cx="7" cy="7" r="6"/><ellipse cx="7" cy="7" rx="2.6" ry="6"/><path d="M1 7h12M2 4h10M2 10h10"/></svg></span>
      </li>
    </ul>

    <p class="services">Restaurant Catering Banquet</p>
  </section>

</body>
</html>
```